Birthday Party Invitation

I need to create a "save the date" for my birthday party.
Text:

Save the Date
Saturday, 6 December 2014
9 pm
Club la Brisa, Lindenweg 42, 8005 Zürich
BLACK IT OUT
SAVE IT!
RESERVE THE TIME
WRITE IT DOWN
HOLD THE DATE to LET YOUR HAIR DOWN and Party with Me.

Target Market(s)

Friends

Industry/Entity Type

Club

Requirements
Must have
• I want the flyer to look classy and sexy at the same time.
Nice to have
• Picture on the left or right, then text white on black background. Maybe a simple frame. Not too playful, rather simple, elegant and no graphics. Just picture and text.

```html
<!DOCTYPE html>
<html lang="en">
<head>
<meta charset="utf-8">
<title>Save the Date – Birthday Party</title>
<link rel="stylesheet" href="https://fonts.googleapis.com/css2?family=Felipa&family=Tinos:ital,wght@1,400;1,700&display=swap">
<style>
  :root {
    --ink-black: #050505;
    --night-grey: #3a3a3a;
    --silver: #cfcfcf;
    --silver-soft: #b9b9b9;
    --caps-white: #e6e6e6;
    --velvet-red: #6e1a14;
    --velvet-deep: #2a0806;
  }
  * { margin: 0; padding: 0; box-sizing: border-box; }
  html, body {
    width: 1200px;
    height: 848px;
    overflow: hidden;
    background: var(--ink-black);
  }
  .invitation {
    position: relative;
    width: 1200px;
    height: 848px;
    overflow: hidden;
    background:
      radial-gradient(ellipse 620px 560px at 330px 250px, var(--night-grey) 0%, #1c1c1c 55%, var(--ink-black) 100%);
  }
  .party-photo {
    position: absolute;
    left: 630px;
    top: 40px;
    width: 570px;
    height: 808px;
    background:
      linear-gradient(to bottom, var(--ink-black) 0%, rgba(5,5,5,0) 25%),
      linear-gradient(to right, rgba(5,5,5,0) 0%, var(--velvet-deep) 18%, var(--velvet-red) 55%, var(--velvet-deep) 100%);
  }
  .headline {
    position: absolute;
    left: 131px;
    top: 78px;
    font-family: "Felipa", serif;
    font-weight: 400;
    font-size: 94px;
    line-height: 1;
    color: var(--silver);
    white-space: nowrap;
  }
  .event-date {
    position: absolute;
    left: 57px;
    top: 190px;
    font-family: "Felipa", serif;
    font-size: 53px;
    line-height: 1;
    color: var(--silver);
    white-space: nowrap;
  }
  .venue {
    position: absolute;
    left: 57px;
    top: 252px;
    font-family: "Felipa", serif;
    font-size: 36px;
    line-height: 1;
    color: var(--silver-soft);
    white-space: nowrap;
  }
  .reminders {
    position: absolute;
    left: 203px;
    top: 426px;
    width: 300px;
    list-style: none;
    text-align: center;
    font-family: "Tinos", serif;
    font-style: italic;
    font-weight: 700;
    font-size: 27px;
    font-variant: small-caps;
    letter-spacing: 0.5px;
    color: var(--caps-white);
    text-shadow: 0 2px 3px rgba(0,0,0,0.9);
  }
  .reminders li { height: 51.5px; line-height: 34px; }
  .closing-line {
    position: absolute;
    left: 0;
    top: 762px;
    width: 1262px;
    text-align: center;
    font-family: "Tinos", serif;
    font-style: italic;
    font-size: 28px;
    line-height: 1.2;
    color: var(--silver);
    white-space: nowrap;
    text-shadow: 0 2px 3px rgba(0,0,0,0.9);
  }
  .closing-line strong { font-weight: 700; font-variant: small-caps; font-size: 30px; }
  .closing-line .script { font-family: "Felipa", serif; font-size: 31px; }
</style>
</head>
<body>
  <main class="invitation">
    <div class="party-photo" role="img" aria-label="Photograph of the host dancing in a red velvet party outfit against a dark background"></div>

    <h1 class="headline">Save the Date</h1>
    <p class="event-date">Saturday, 6 December 2014 9 pm</p>
    <p class="venue">Club la Brisa, Lindenweg 42, 8005 Zürich</p>

    <ul class="reminders">
      <li>Black it out</li>
      <li>Save it!</li>
      <li>Reserve the time</li>
      <li>Write it down</li>
    </ul>

    <p class="closing-line"><strong>Hold the date</strong> to <strong>Let your hair down</strong> <span class="script">and party with me!</span></p>
  </main>
</body>
</html>
```